Trailer Lettering or Partial Wrap

I purchased a new gloss black 7' wide x 12' long x 7' height enclosed cargo trailer that I would like to brand for advertising. on all 4 sides. Our font is AgencyFB (and we only use lower case letters). To reduce cost I thought using the black gloss background could be achieved and use cut out vinyl rather than full wrap unless there are some other ideas. Our colors are Black, White, and Red (HEX #BE1E2D. Items to be displayed:
- logo
- phone # (405) 555-0147
- email. catering@thekelpdockok.com
- web address: www.thekelpdockok.com
- our 2 restaurant locations
- "Edmond" 4870 SE 52nd, Edmond OK 73025
- "NW-OKC" 2915 E Larkspur Rd, Oklahoma City, OK 73159

we would also like to highlight 3 services we offer:
- Catering
- Rent-A-Chef Events
- Sushi Making Classes

For reference our chopsticks from the logo files we use on a lot of print items. Not that I want it to be like this, but I did attach a sample of what ChatGPT created though is in an unusable format and fonts aren't consistent. As well a recent 2' x 4' sign we had made to use on table displays.

We also do like the wording on that last item of " Sushi | Experience | Elevated"

```html
<!DOCTYPE html>
<html lang="en">
<head>
<meta charset="utf-8">
<title>the kelp dock — trailer lettering layout</title>
<link href="https://fonts.googleapis.com/css2?family=Saira+Extra+Condensed:wght@400;500&display=swap" rel="stylesheet">
<style>
  :root {
    --gloss-black: #0d0d0e;
    --brand-red: #be1e2d;
    --white: #ffffff;
    --trim: #b9bcc0;
    --plate: #a9adb2;
    --backdrop: #e6e7e9;
  }
  * { margin: 0; padding: 0; box-sizing: border-box; }
  html, body { width: 806px; height: 1200px; overflow: hidden; background: var(--backdrop); }
  body { position: relative; font-family: "Saira Extra Condensed", "Arial Narrow", sans-serif; color: var(--white); font-weight: 500; }

  .panel { position: absolute; background: var(--gloss-black); overflow: hidden; }
  .side-curb { left: 73px; top: 11px; width: 660px; height: 385px; }
  .side-road { left: 73px; top: 407px; width: 660px; height: 385px; }
  .end-front { left: 13px; top: 803px; width: 385px; height: 385px; }
  .end-rear { left: 408px; top: 803px; width: 385px; height: 385px; }

  .abs { position: absolute; }
  .brand { display: flex; align-items: center; gap: 10px; }
  .brand-dot { border: 4px solid var(--brand-red); border-radius: 50%; flex: none; }
  .brand-name { line-height: 0.86; color: var(--white); font-weight: 500; white-space: nowrap; }

  .service { display: flex; align-items: center; gap: 10px; color: var(--brand-red); white-space: nowrap; }
  .service-icon { border: 2px solid var(--white); border-radius: 50%; flex: none; }

  .phone { color: var(--white); line-height: 1; white-space: nowrap; }
  .email { color: var(--white); white-space: nowrap; }
  .red-band { background: var(--brand-red); color: var(--white); display: inline-block; padding: 0 10px; white-space: nowrap; line-height: 1.25; }
  .tagline { white-space: nowrap; }

  .door { border: 3px solid var(--trim); }
  .swoosh { position: absolute; }
  .plate { position: absolute; background: linear-gradient(135deg, #c4c7cb, var(--plate)); }

  .location { text-align: center; }
  .location-name { line-height: 1; }
  .location-addr { font-size: 10px; font-weight: 400; white-space: nowrap; }
  .divider { position: absolute; width: 2px; background: var(--brand-red); }
</style>
</head>
<body>

<!-- Curbside panel with entry door -->
<section class="panel side-curb">
  <svg class="swoosh" role="img" aria-label="red brush stroke sweeping across the lower panel" width="660" height="385" viewBox="0 0 660 385" style="left:0; top:0;">
    <path d="M330 385 C420 360 520 320 600 220 C630 180 650 130 660 100 L660 170 C630 250 560 330 420 385 Z" fill="var(--brand-red)"/>
  </svg>

  <div class="brand abs" style="left:26px; top:40px;">
    <span class="brand-dot" style="width:24px; height:24px;"></span>
    <span class="brand-name" style="font-size:56px;">the<br>kelp<br>dock</span>
  </div>
  <div class="email abs" style="left:30px; top:232px; font-size:13px;">catering@thekelpdockok.com</div>
  <div class="abs" style="left:30px; top:253px;"><span class="red-band" style="font-size:13px;">www.thekelpdockok.com</span></div>
  <div class="phone abs" style="left:26px; top:284px; font-size:38px;">(405) 555-0147</div>

  <div class="abs" style="left:205px; top:50px;">
    <div class="service" style="font-size:19px; margin-bottom:44px;"><span class="service-icon" role="img" aria-label="catering icon" style="width:34px; height:34px;"></span>Catering</div>
    <div class="service" style="font-size:19px; margin-bottom:44px;"><span class="service-icon" role="img" aria-label="chef icon" style="width:34px; height:34px;"></span>Rent-A-Chef Events</div>
    <div class="service" style="font-size:19px;"><span class="service-icon" role="img" aria-label="sushi roll icon" style="width:34px; height:34px;"></span>Sushi Making Classes</div>
  </div>

  <div class="door abs" style="left:455px; top:40px; width:140px; height:335px;"></div>
</section>

<!-- Roadside panel -->
<section class="panel side-road">
  <svg class="swoosh" role="img" aria-label="red brush stroke along the lower left edge" width="660" height="385" viewBox="0 0 660 385" style="left:0; top:0;">
    <path d="M0 200 C20 270 60 330 120 385 L80 385 C40 340 10 290 0 250 Z" fill="var(--brand-red)"/>
  </svg>

  <div class="abs" style="left:30px; top:38px;">
    <div class="service" style="font-size:17px; margin-bottom:16px;"><span class="service-icon" role="img" aria-label="catering icon" style="width:26px; height:26px;"></span>Catering</div>
    <div class="service" style="font-size:17px; margin-bottom:16px;"><span class="service-icon" role="img" aria-label="chef icon" style="width:26px; height:26px;"></span>Rent-A-Chef Events</div>
    <div class="service" style="font-size:17px;"><span class="service-icon" role="img" aria-label="sushi roll icon" style="width:26px; height:26px;"></span>Sushi Making Classes</div>
  </div>

  <div class="brand abs" style="left:330px; top:34px;">
    <span class="brand-dot" style="width:32px; height:32px;"></span>
    <span class="brand-name" style="font-size:72px;">the<br>kelp<br>dock</span>
  </div>

  <div class="phone abs" style="left:36px; top:236px; font-size:38px;">(405) 555-0147</div>
  <div class="email abs" style="left:345px; top:250px; font-size:22px;">catering@thekelpdockok.com</div>
  <div class="abs" style="left:345px; top:288px;"><span class="red-band" style="font-size:22px;">www.thekelpdockok.com</span></div>
</section>

<!-- Front panel -->
<section class="panel end-front">
  <div class="brand abs" style="left:0; width:385px; top:40px; justify-content:center;">
    <span class="brand-dot" style="width:20px; height:20px;"></span>
    <span class="brand-name" style="font-size:46px;">the kelp dock</span>
  </div>
  <div class="abs" style="left:0; width:385px; top:108px; text-align:center;"><span class="red-band" style="font-size:28px;">(405) 555-0147</span></div>
  <div class="tagline abs" style="left:0; width:385px; top:150px; text-align:center; font-size:15px; font-weight:400;">Sushi | Experience | Elevated</div>
  <div class="location abs" style="left:0; width:385px; top:178px;">
    <svg width="18" height="26" viewBox="0 0 18 26" aria-hidden="true"><path d="M9 0C4 0 0 4 0 9c0 7 9 17 9 17s9-10 9-17C18 4 14 0 9 0z" fill="var(--brand-red)"/><circle cx="9" cy="9" r="3.5" fill="var(--gloss-black)"/></svg>
    <div class="location-name" style="font-size:34px;">Edmond</div>
    <div class="location-addr">4870 SE 52nd, Edmond OK 73025</div>
  </div>
  <div class="plate" role="img" aria-label="aluminium diamond plate stone guard" style="left:0; bottom:0; width:385px; height:92px;"></div>
</section>

<!-- Rear panel -->
<section class="panel end-rear">
  <div class="brand abs" style="left:0; width:385px; top:24px; justify-content:center;">
    <span class="brand-dot" style="width:22px; height:22px;"></span>
    <span class="brand-name" style="font-size:44px;">the<br>kelp<br>dock</span>
  </div>
  <div class="phone abs" style="left:0; width:385px; top:164px; text-align:center; font-size:40px;">(405) 555-0147</div>
  <div class="abs" style="left:0; width:385px; top:214px; text-align:center;"><span class="red-band tagline" style="font-size:16px;">Sushi | Experience | Elevated</span></div>

  <div class="location abs" style="left:12px; width:172px; top:262px;">
    <svg width="16" height="23" viewBox="0 0 18 26" aria-hidden="true"><path d="M9 0C4 0 0 4 0 9c0 7 9 17 9 17s9-10 9-17C18 4 14 0 9 0z" fill="var(--brand-red)"/><circle cx="9" cy="9" r="3.5" fill="var(--gloss-black)"/></svg>
    <div class="location-name" style="font-size:30px;">Edmond</div>
    <div class="location-addr" style="font-size:9px;">4870 SE 52nd, Edmond OK 73025</div>
  </div>
  <div class="divider" style="left:192px; top:268px; height:90px;"></div>
  <div class="location abs" style="left:198px; width:180px; top:262px;">
    <svg width="16" height="23" viewBox="0 0 18 26" aria-hidden="true"><path d="M9 0C4 0 0 4 0 9c0 7 9 17 9 17s9-10 9-17C18 4 14 0 9 0z" fill="var(--brand-red)"/><circle cx="9" cy="9" r="3.5" fill="var(--gloss-black)"/></svg>
    <div class="location-name" style="font-size:30px;">NW-OKC</div>
    <div class="location-addr" style="font-size:8px;">2915 E Larkspur Rd, Oklahoma City, OK 73159</div>
  </div>
</section>

</body>
</html>
```